Blueberry Road side sign

I want a sign to put on the side of the road to advertise the that I have fresh local blueberries for sale. attatched is my company logo.
I want to use the same font that is used in my logo design.
I want "blueberries" written across the sign,
with maybe a couple of berries after the writing.

```html
<!DOCTYPE html>
<html lang="en">
<head>
<meta charset="utf-8">
<title>Fresh Local Blueberry For Sale – Roadside Sign</title>
<link rel="stylesheet" href="https://fonts.googleapis.com/css2?family=Open+Sans:wght@700&family=Pacifico&display=swap">
<style>
  :root {
    --sign-white: #ffffff;
    --brand-navy: #1f4596;
    --brand-blue: #1d4f9f;
    --accent-orange: #f7ab1c;
    --berry-light: #c9d3e3;
    --berry-mid: #9fb0cc;
  }
  html, body {
    margin: 0;
    padding: 0;
    overflow: hidden;
    background: var(--sign-white);
  }
  .sign {
    position: relative;
    width: 1200px;
    height: 600px;
    overflow: hidden;
    background: var(--sign-white);
  }
  .brand-panel {
    position: absolute;
    left: 0;
    top: 0;
    width: 430px;
    height: 125px;
    background: var(--brand-blue);
    display: flex;
    align-items: center;
    gap: 22px;
    padding-left: 52px;
    box-sizing: border-box;
  }
  .brand-dot {
    width: 62px;
    height: 62px;
    border-radius: 50%;
    background: var(--sign-white);
  }
  .brand-name {
    font-family: "Pacifico", cursive;
    font-size: 42px;
    color: var(--sign-white);
    line-height: 1;
  }
  .berry-photo {
    position: absolute;
    left: 444px;
    top: 0;
    width: 706px;
    height: 576px;
    border-radius: 48% 42% 46% 50%;
    background:
      radial-gradient(ellipse at 70% 20%, rgba(150, 200, 120, 0.55) 0 12%, transparent 26%),
      radial-gradient(ellipse at 50% 55%, var(--berry-mid) 0%, var(--berry-light) 55%, rgba(255,255,255,0) 72%);
  }
  .headline {
    position: absolute;
    left: 0;
    top: 0;
    width: 1200px;
    height: 600px;
  }
  .headline text {
    paint-order: stroke fill;
    stroke-linejoin: round;
  }
  .tagline {
    font-family: "Open Sans", sans-serif;
    font-weight: 700;
    fill: var(--accent-orange);
    stroke: var(--brand-navy);
    stroke-width: 5px;
  }
  .product-word {
    font-family: "Pacifico", cursive;
    font-size: 262px;
    fill: var(--brand-navy);
    stroke: var(--sign-white);
    stroke-width: 12px;
  }
  .footer-band {
    position: absolute;
    left: 0;
    bottom: 0;
    width: 1200px;
    height: 20px;
    background: var(--brand-blue);
  }
</style>
</head>
<body>
  <main class="sign">
    <div class="berry-photo" role="img" aria-label="Photo of a pile of fresh blueberries with a few green leaves"></div>

    <header class="brand-panel">
      <span class="brand-dot"></span>
      <span class="brand-name">Kettle Creek</span>
    </header>

    <svg class="headline" viewBox="0 0 1200 600" aria-label="Fresh local blueberry for sale">
      <defs>
        <filter id="word-shadow" x="-5%" y="-5%" width="110%" height="120%">
          <feDropShadow dx="3" dy="5" stdDeviation="4" flood-color="#0b1d45" flood-opacity="0.35"/>
        </filter>
      </defs>
      <g class="product-word" filter="url(#word-shadow)">
        <text x="78" y="428" textLength="470" lengthAdjust="spacingAndGlyphs">Blue</text>
        <text x="540" y="428" textLength="596" lengthAdjust="spacingAndGlyphs">berry</text>
      </g>
      <text class="tagline" x="684" y="202" font-size="70" textLength="452" lengthAdjust="spacingAndGlyphs">FRESH LOCAL</text>
      <text class="tagline" x="108" y="532" font-size="76" textLength="366" lengthAdjust="spacingAndGlyphs">FOR SALE</text>
    </svg>

    <div class="footer-band"></div>
  </main>
</body>
</html>
```